Moder Business Card Design for Renewables Business

Need a business card design for my business. We collect & repurpose spent coffee ground from cafes. The cards will be made from recycled paper. Needs to fit our corporate colour scheme of white, green & brown (see logo for colour codes). Eco friendly, modern, intresting & eye catching.
This card needs to convey the message of the business and fit into its mantra of eco-friendly, sustainable etc.

Target Market(s)

Cafe Owners, Coffee Drinkers, Recycling Companies, Farmers

Industry/Entity Type

Recycling

Contact Information for Business Card

Name; Peter Halloran
Phone; 0412 386 527
e-mail; info@lumatrove.com.au
website; www.lumatrove.com.au

Font styles to use
Sans Serif
Script

Colors

Designer to choose colors to be used in the design.

Requirements
Must have
• FRONT;
• Logo, Name (Peter Halloran), phone number, e-mail address, website
• BACK;
• On the back in cursive text; 'SUSTAINABILITY IN THE DAILY GRIND'
• Small facebook & Instagram logos with text 'Lumatrove'
Should not have
• messy design

```html
<!DOCTYPE html>
<html lang="en">
<head>
<meta charset="utf-8">
<title>Lumatrove Business Card</title>
<link rel="stylesheet" href="https://fonts.googleapis.com/css2?family=Josefin+Sans:wght@700&family=Questrial&display=swap">
<style>
  :root {
    --brown: #5f2f10;
    --green: #79a83a;
    --paper: #ffffff;
  }
  html, body {
    margin: 0;
    padding: 0;
    overflow: hidden;
    background: var(--paper);
  }
  .card {
    position: relative;
    width: 1200px;
    height: 720px;
    background: var(--paper);
    overflow: hidden;
  }
  .brand {
    position: absolute;
    left: 190px;
    top: 254px;
    width: 320px;
    text-align: center;
  }
  .brand-mark {
    display: block;
    margin: 0 auto;
  }
  .brand-name {
    margin: 14px 0 0;
    font-family: "Questrial", sans-serif;
    font-size: 48px;
    line-height: 1;
    color: var(--green);
    letter-spacing: 1px;
    text-transform: uppercase;
  }
  .holder-name {
    position: absolute;
    left: 769px;
    top: 280px;
    margin: 0;
    font-family: "Josefin Sans", sans-serif;
    font-weight: 700;
    font-size: 25px;
    letter-spacing: 2.6px;
    color: var(--brown);
    text-transform: uppercase;
  }
  .contacts {
    position: absolute;
    left: 689px;
    top: 365px;
    margin: 0;
    padding: 0;
    list-style: none;
  }
  .contact {
    display: flex;
    align-items: center;
    height: 50px;
    margin-bottom: 40px;
  }
  .contact-icon {
    width: 32px;
    height: 32px;
    fill: var(--brown);
    flex: none;
  }
  .contact-text {
    margin-left: 52px;
    font-family: "Questrial", sans-serif;
    font-size: 25px;
    letter-spacing: 3px;
    color: var(--green);
  }
</style>
</head>
<body>
<main class="card">
  <section class="brand">
    <svg class="brand-mark" width="256" height="256" viewBox="0 0 256 256" aria-hidden="true">
      <circle cx="128" cy="128" r="120" fill="none" stroke="var(--brown)" stroke-width="14"/>
    </svg>
    <p class="brand-name">Lumatrove</p>
  </section>

  <h1 class="holder-name">Peter Halloran</h1>

  <ul class="contacts">
    <li class="contact">
      <svg class="contact-icon" viewBox="0 0 32 32" aria-hidden="true">
        <path d="M7 2c1.2-.6 2.3-.2 3 .8l3 4.6c.6 1 .4 2.2-.5 3l-2 1.6c1.3 3.4 4 6.6 7.2 8.5l1.8-1.8c.9-.8 2.1-.9 3-.2l4.5 3.2c1 .7 1.3 1.9.6 3l-1.4 2.2c-1 1.6-3 2.3-4.8 1.6C12.8 25.8 5.5 17.8 3.2 9c-.5-1.9.3-3.8 2-4.8z"/>
      </svg>
      <span class="contact-text">0412386527</span>
    </li>
    <li class="contact">
      <svg class="contact-icon" viewBox="0 0 32 32" aria-hidden="true">
        <path d="M1 7h30v2L16 19 1 9z"/>
        <path d="M1 12l15 10 15-10v13H1z"/>
      </svg>
      <span class="contact-text">info@lumatrove.com.au</span>
    </li>
    <li class="contact">
      <svg class="contact-icon" viewBox="0 0 32 32" aria-hidden="true">
        <path d="M16 2L1 15.5l2 2.2 2-1.8V30h8v-8h6v8h8V15.9l2 1.8 2-2.2z"/>
      </svg>
      <span class="contact-text">www.lumatrove.com.au</span>
    </li>
  </ul>
</main>
</body>
</html>
```